Digital & Print Graphic Design templates for Comedy Club

We need new new digital & print graphic design templates for our upcoming comedy events created for use in CANVA in the following specs
Digital:
1080x1080px
1200x600px
800x400px
1920x1080px
1080x1355px
1500x500px
851x315px
Print
11x17"
22x28"
95.5x30"

Target Market(s)

18+ comedy fans

Industry/Entity Type

comedy club

Font styles to use
Sans Serif

Colors
FFF300
FFF600
FEFA6F
FFFEC7
FFFEE8
6B429C
8869AF
B7A5CE
E3DAEB
F3F0F8

Requirements
Must have
• templates must be CANVA compatible. frame for comedian photo.
Nice to have
• would like to incorporate deep purple into the design
Should not have
• do not include phone number on any templates

```html
<!DOCTYPE html>
<html lang="en">
<head>
<meta charset="UTF-8">
<title>Tom Vance – Live at Chuckle Den</title>
<link href="https://fonts.googleapis.com/css2?family=Bowlby+One&family=Righteous&display=swap" rel="stylesheet">
<style>
  :root {
    --surround: #b1b2b4;
    --paper: #ffffff;
    --deep-purple: #3a1968;
    --night-purple: #2a0f52;
    --brand-purple: #4b2486;
    --yellow: #f2e21f;
    --ink: #0c0c0c;
    --edge-red: #e0211c;
  }
  html, body {
    margin: 0;
    width: 1178px;
    height: 1200px;
    overflow: hidden;
    background: var(--surround);
  }
  .poster {
    position: absolute;
    left: 81px;
    top: 86px;
    width: 1016px;
    height: 1015px;
    display: block;
  }
  .headline {
    font-family: "Righteous", sans-serif;
    font-size: 82px;
    letter-spacing: 9px;
    fill: var(--yellow);
  }
  .club-name {
    font-family: "Righteous", sans-serif;
    font-size: 46px;
    fill: var(--yellow);
  }
  .performer {
    font-family: "Bowlby One", sans-serif;
  }
  .event-date {
    font-family: "Righteous", sans-serif;
    font-size: 64px;
    letter-spacing: 8px;
    fill: var(--brand-purple);
  }
</style>
</head>
<body>
<svg class="poster" viewBox="0 0 1016 1015" xmlns="http://www.w3.org/2000/svg">
  <defs>
    <radialGradient id="stage-glow" cx="0.6" cy="0.45" r="0.7">
      <stop offset="0" stop-color="#4a2680"/>
      <stop offset="1" stop-color="var(--night-purple)"/>
    </radialGradient>
    <linearGradient id="portrait-tone" x1="0" y1="0" x2="0" y2="1">
      <stop offset="0" stop-color="#b88a72"/>
      <stop offset="0.3" stop-color="#8a6a5c"/>
      <stop offset="0.45" stop-color="#1d1d1f"/>
      <stop offset="1" stop-color="#111113"/>
    </linearGradient>
  </defs>

  <!-- stage backdrop -->
  <rect class="backdrop" width="1016" height="1015" fill="url(#stage-glow)"/>
  <path class="top-sweep" d="M0 0 H1016 V30 C 860 90 720 150 560 150 C 380 150 200 70 0 38 Z" fill="var(--paper)"/>
  <path class="bottom-sweep" d="M0 1015 V945 C 250 905 700 880 1016 932 V1015 Z" fill="var(--paper)"/>

  <!-- comedian photo frame -->
  <path class="photo-frame" role="img" aria-label="Comedian photo: performer holding a microphone, shocked expression"
        d="M500 42 C 560 25 640 40 652 112 L 660 205 L 770 262 C 825 292 852 342 862 402 L 880 660 L 700 720 L 430 900 L 238 720 L 258 400 C 268 320 330 282 400 262 L 480 222 L 470 130 C 470 82 480 52 500 42 Z"
        fill="url(#portrait-tone)" stroke="var(--yellow)" stroke-width="6"/>

  <!-- headline -->
  <text class="headline" x="37" y="251">LIVE AT</text>
  <text class="headline" x="37" y="360">CHUCKLE</text>
  <text class="headline" x="37" y="468">DEN</text>

  <!-- club mark -->
  <g class="club-mark">
    <circle cx="832" cy="149" r="130" fill="var(--ink)" stroke="var(--yellow)" stroke-width="4"/>
    <text class="club-name" x="832" y="142" text-anchor="middle">CHUCKLE</text>
    <text class="club-name" x="832" y="192" text-anchor="middle">DEN</text>
  </g>

  <!-- performer name -->
  <g class="performer">
    <text x="379" y="712" font-size="285" textLength="403" lengthAdjust="spacingAndGlyphs" fill="var(--ink)">TOM</text>
    <text x="385" y="708" font-size="285" textLength="403" lengthAdjust="spacingAndGlyphs" fill="var(--edge-red)">TOM</text>
    <text x="389" y="706" font-size="285" textLength="403" lengthAdjust="spacingAndGlyphs" fill="var(--yellow)">TOM</text>

    <text x="132" y="929" font-size="320" textLength="644" lengthAdjust="spacingAndGlyphs" fill="var(--ink)">VANCE</text>
    <text x="138" y="925" font-size="320" textLength="644" lengthAdjust="spacingAndGlyphs" fill="var(--edge-red)">VANCE</text>
    <text x="142" y="923" font-size="320" textLength="644" lengthAdjust="spacingAndGlyphs" fill="var(--yellow)">VANCE</text>
  </g>

  <!-- date -->
  <text class="event-date" x="498" y="1006" text-anchor="middle">4TH FEB , 2026</text>
</svg>
</body>
</html>
```